Retractable Banners for Ridgeway Talent Alliance

We need to have 2 different retractable banners designed that will be used at a variety of events. We plan to have the banners printed through printovera.com. According to their site, specs are as follows:

Retractable banners are digitally printed on 12oz double-sided smooth vinyl. While the area on the retractable banners is 33 x 78, the customer will want to provide a file that has an area of 35 x 82 to account for bleed, with 3" of that vertical bleed at the bottom of the design. Recommended DPI is 150. Upload capacity for Retractable Banners is 100MP.

Banner #1:
Ridgeway Talent Alliance logo at top

Then the following text placed lower on the banner:

Creating Positive Impacts for Alder County Businesses (Heading)

Body of text: Ridgeway Talent Alliance is committed to enhancing the region's ability to meet the workforce needs of local employers through the investments of federal and state funds.

Banner #2:

Meeting the workforce needs of employers and individuals through partnerships and innovation.

You can check out some of our images (water drop, waves) and color schemes we use on our website at ridgewaytalent.org.

Target Market(s)

Job seekers, workforce development professionals, city leaders, company CEO's, community members, elected officials.

Industry/Entity Type

Events

Font styles to use
Serif
Sans Serif

Requirements
Must have
• -Be easy to read and understand
• - Must include Ridgeway Talent Alliance logo and text provided for each banner
Nice to have
• color ideas for banners: #0655a3; #0393ce; #00a990; #0355a3; #00a990; #33a6d7
Should not have
• Nothing that depicts gender

```html
<!DOCTYPE html>
<html lang="en">
<head>
<meta charset="utf-8">
<title>Ridgeway Talent Alliance – Retractable Banners</title>
<link href="https://fonts.googleapis.com/css2?family=Open+Sans:wght@300;400;600;700&display=swap" rel="stylesheet">
<style>
  :root {
    --page-bg: #eef0f3;
    --white: #ffffff;
    --brand-blue: #0355a3;
    --navy-top: #2a67b0;
    --navy-mid: #163f82;
    --navy-deep: #0c2457;
    --accent-green: #3fae8d;
    --line-blue: #1f4f9a;
    --url-green: #5fbfa2;
    --forest-light: #c2a56a;
    --forest-dark: #5d4c2c;
    --water-light: #a9bdd6;
    --water-dark: #1d3a68;
  }
  * { margin: 0; padding: 0; box-sizing: border-box; }
  html, body { width: 1200px; height: 1119px; overflow: hidden; }
  body {
    background: var(--page-bg);
    font-family: "Open Sans", Arial, sans-serif;
    position: relative;
  }
  .banner {
    position: absolute;
    top: 70px;
    width: 330px;
    height: 980px;
    background: var(--white);
    box-shadow: 0 4px 18px rgba(0,0,0,0.12);
    overflow: hidden;
  }
  .banner--mission { left: 180px; }
  .banner--impact { left: 690px; }
  .banner__art { position: absolute; inset: 0; width: 330px; height: 980px; }

  .brand {
    position: absolute;
    display: flex;
    align-items: center;
    gap: 7px;
    color: var(--brand-blue);
    font-weight: 700;
    font-size: 12px;
    letter-spacing: 0.4px;
    white-space: nowrap;
  }
  .brand__mark {
    width: 14px; height: 14px; border-radius: 50%;
    background: var(--brand-blue);
  }
  .banner--mission .brand { top: 22px; right: 14px; }
  .banner--impact .brand { top: 58px; left: 58px; }

  .mission-statement {
    position: absolute;
    left: 16px;
    top: 540px;
    width: 300px;
    font-size: 22px;
    line-height: 45px;
    text-transform: uppercase;
    color: var(--white);
  }
  .mission-statement .light { font-weight: 300; font-size: 24px; }
  .mission-statement .strong { font-weight: 700; color: var(--accent-green); letter-spacing: 0.2px; }

  .impact-heading {
    position: absolute;
    right: 16px;
    top: 112px;
    text-align: right;
    text-transform: uppercase;
    font-weight: 300;
    font-size: 30px;
    line-height: 48px;
    color: var(--line-blue);
  }
  .impact-heading .strong { font-weight: 700; color: var(--accent-green); }

  .impact-body {
    position: absolute;
    left: 14px;
    top: 676px;
    width: 300px;
    font-size: 14px;
    line-height: 33px;
    color: var(--white);
  }
  .impact-body .org { font-weight: 700; color: var(--accent-green); text-transform: uppercase; font-size: 13px; }

  .site-rule {
    position: absolute;
    left: 22px; right: 22px;
    height: 1px;
    background: rgba(255,255,255,0.45);
  }
  .site-url {
    position: absolute;
    left: 0; right: 0;
    text-align: center;
    font-size: 10px;
    letter-spacing: 4px;
    text-transform: uppercase;
    color: var(--url-green);
  }
  .banner--mission .site-rule { top: 898px; }
  .banner--mission .site-url { top: 912px; }
  .banner--impact .site-rule { top: 886px; }
  .banner--impact .site-url { top: 900px; }
</style>
</head>
<body>

<section class="banner banner--mission">
  <svg class="banner__art" viewBox="0 0 330 980" aria-hidden="true">
    <defs>
      <linearGradient id="forestTone" x1="0" y1="0" x2="0" y2="1">
        <stop offset="0" stop-color="var(--forest-dark)"/>
        <stop offset="0.6" stop-color="var(--forest-light)"/>
        <stop offset="1" stop-color="var(--forest-dark)"/>
      </linearGradient>
      <linearGradient id="navyFadeA" x1="0" y1="0" x2="0" y2="1">
        <stop offset="0" stop-color="var(--navy-top)"/>
        <stop offset="0.5" stop-color="var(--navy-mid)"/>
        <stop offset="1" stop-color="var(--navy-deep)"/>
      </linearGradient>
    </defs>
    <g role="img" aria-label="Photo of a leaf-covered path through a tall tree avenue">
      <polygon points="0,60 330,250 330,540 0,350" fill="url(#forestTone)"/>
    </g>
    <line x1="70" y1="62" x2="330" y2="212" stroke="var(--line-blue)" stroke-width="2"/>
    <line x1="120" y1="78" x2="330" y2="198" stroke="var(--line-blue)" stroke-width="1.5"/>
    <polygon points="0,340 330,515 330,980 0,980" fill="url(#navyFadeA)"/>
    <line x1="0" y1="352" x2="300" y2="515" stroke="var(--white)" stroke-width="2"/>
    <line x1="70" y1="375" x2="290" y2="495" stroke="var(--white)" stroke-width="1.5"/>
  </svg>

  <div class="brand"><span class="brand__mark"></span>RIDGEWAY TALENT ALLIANCE</div>

  <p class="mission-statement">
    <span class="light">Meeting</span><br>
    <span class="strong">The workforce</span><br>
    <span class="strong">needs of employers</span><br>
    <span class="strong">and individuals</span><br>
    <span class="light">Through</span><br>
    <span class="strong">partnerships and</span><br>
    <span class="strong">innovation</span>
  </p>

  <div class="site-rule"></div>
  <div class="site-url">www.ridgewaytalent.org</div>
</section>

<section class="banner banner--impact">
  <svg class="banner__art" viewBox="0 0 330 980" aria-hidden="true">
    <defs>
      <radialGradient id="waterTone" cx="0.55" cy="0.55" r="0.7">
        <stop offset="0" stop-color="var(--water-light)"/>
        <stop offset="0.55" stop-color="#5678a4"/>
        <stop offset="1" stop-color="var(--water-dark)"/>
      </radialGradient>
      <linearGradient id="navyFadeB" x1="0" y1="0" x2="0" y2="1">
        <stop offset="0" stop-color="var(--navy-mid)"/>
        <stop offset="1" stop-color="var(--navy-deep)"/>
      </linearGradient>
    </defs>
    <g role="img" aria-label="Photo of a water drop falling into rippling blue water">
      <polygon points="0,272 330,432 330,740 0,590" fill="url(#waterTone)"/>
    </g>
    <line x1="0" y1="262" x2="330" y2="424" stroke="var(--line-blue)" stroke-width="2"/>
    <line x1="70" y1="282" x2="290" y2="390" stroke="var(--line-blue)" stroke-width="1.5"/>
    <polygon points="0,600 330,760 330,980 0,980" fill="url(#navyFadeB)"/>
    <line x1="0" y1="585" x2="300" y2="735" stroke="var(--white)" stroke-width="2"/>
    <line x1="90" y1="612" x2="290" y2="712" stroke="var(--white)" stroke-width="1.5"/>
  </svg>

  <div class="brand"><span class="brand__mark"></span>RIDGEWAY TALENT ALLIANCE</div>

  <h2 class="impact-heading">
    Creating<br>
    <span class="strong">Positive Impacts</span><br>
    For Alder County<br>
    Businesses
  </h2>

  <p class="impact-body">
    <span class="org">Ridgeway Talent</span><br>
    <span class="org">Alliance</span> is committed<br>
    to enhancing the region’s ability<br>
    to meet the workforce needs of local<br>
    employers through the investments of<br>
    federal and state funds
  </p>

  <div class="site-rule"></div>
  <div class="site-url">www.ridgewaytalent.org</div>
</section>

</body>
</html>
```